banner ad

We're looking for a banner similar to the one shown on the attached file. The same 4 keywords, the same text up top, but with new formatting, design and perhaps color scheme. Looking for something to catch people's attention that will stand out on this particular page shown in the attached image. Our goal is to find a banner with a better click through rate than the current version.

```html
<!DOCTYPE html>
<html lang="en">
<head>
<meta charset="utf-8">
<title>Ads Related to Blood Glucose – Banner Variations</title>
<link rel="stylesheet" href="https://fonts.googleapis.com/css2?family=Ubuntu:wght@400;500&display=swap">
<style>
  :root {
    --canvas: #ffffff;
    --pink-bg: #f7d1d1;
    --pink-border: #c98a8a;
    --plain-border: #8a8a8a;
    --red-bar: #b3272b;
    --red-bar-dark: #8e0c10;
    --black-bar: #262626;
    --black-bar-dark: #111111;
    --pill-top: #3a3a3a;
    --pill-bottom: #000000;
    --pill-ring: #bdbdbd;
    --blood: #c4080d;
    --blood-dark: #6e0004;
    --label: #e4e4e4;
    --white: #ffffff;
  }
  * { box-sizing: border-box; margin: 0; padding: 0; }
  html, body {
    width: 1200px; height: 960px; overflow: hidden;
    background: var(--canvas);
    font-family: "Ubuntu", sans-serif;
  }
  .canvas { position: relative; width: 1200px; height: 960px; }

  .ad-unit {
    position: absolute; left: 34px; width: 1139px; height: 262px;
    border: 2px solid var(--pink-border);
    background: var(--pink-bg);
  }
  .ad-unit--plain { background: var(--white); border-color: var(--plain-border); }
  .ad-unit--one { top: 61px; }
  .ad-unit--two { top: 352px; }
  .ad-unit--three { top: 645px; }

  .ad-header {
    position: absolute; left: 7px; top: 7px; width: 1122px; height: 53px;
    background: linear-gradient(var(--black-bar) 0 72%, var(--black-bar-dark) 72% 100%);
    color: var(--white);
    display: flex; align-items: center; justify-content: space-between;
    padding: 0 12px 4px 14px;
  }
  .ad-header--red {
    background: linear-gradient(var(--red-bar) 0 72%, var(--red-bar-dark) 72% 100%);
  }
  .ad-title { font-size: 34px; font-weight: 400; letter-spacing: 0.2px; }
  .ad-label { font-size: 19px; letter-spacing: 0.3px; }

  .ad-fold { position: absolute; left: 7px; top: 60px; width: 12px; height: 22px; }

  .keyword {
    position: absolute; width: 507px; height: 74px;
    border-radius: 37px;
    border: 3px solid var(--pill-ring);
    box-shadow: 0 0 0 2px #555 inset;
    background: linear-gradient(var(--pill-top), var(--pill-bottom) 55%, #151515);
    overflow: hidden;
    display: flex; align-items: center; justify-content: center;
    color: var(--label); text-decoration: none;
    font-size: 32px; letter-spacing: 1.2px;
    text-shadow: 0 2px 3px #000;
  }
  .keyword__drip {
    position: absolute; left: 0; top: 0; width: 330px; height: 60px;
    background: radial-gradient(ellipse 60% 45% at 35% 10%, var(--blood) 60%, transparent 62%),
                linear-gradient(90deg, var(--blood-dark), var(--blood) 40%, rgba(196,8,13,0) 100%);
    -webkit-mask: linear-gradient(#000 0 40%, transparent 60%);
    mask: linear-gradient(#000 0 40%, transparent 60%);
  }
  .keyword__text { position: relative; }
  .col-a { left: 32px; } .col-b { left: 589px; }
  .row-a { top: 80px; } .row-b { top: 170px; }
</style>
</head>
<body>
<div class="canvas">

  <section class="ad-unit ad-unit--one">
    <header class="ad-header ad-header--red">
      <h2 class="ad-title">Ads Related to Blood Glucose</h2>
      <span class="ad-label">ADVERTISEMENT</span>
    </header>
    <svg class="ad-fold" viewBox="0 0 12 22"><polygon points="0,0 12,0 0,22" fill="#111"/></svg>
    <a class="keyword col-a row-a" href="#"><span class="keyword__drip" role="img" aria-label="Dripping blood decoration"></span><span class="keyword__text">Blood Glucose</span></a>
    <a class="keyword col-b row-a" href="#"><span class="keyword__drip" role="img" aria-label="Dripping blood decoration"></span><span class="keyword__text">Blood Sugar Levels Chart</span></a>
    <a class="keyword col-a row-b" href="#"><span class="keyword__drip" role="img" aria-label="Dripping blood decoration"></span><span class="keyword__text">Normal Blood Sugar Range</span></a>
    <a class="keyword col-b row-b" href="#"><span class="keyword__drip" role="img" aria-label="Dripping blood decoration"></span><span class="keyword__text">Normal Blood Sugar Range</span></a>
  </section>

  <section class="ad-unit ad-unit--plain ad-unit--two">
    <header class="ad-header">
      <h2 class="ad-title">Ads Related to Blood Glucose</h2>
      <span class="ad-label">ADVERTISEMENT</span>
    </header>
    <svg class="ad-fold" viewBox="0 0 12 22"><polygon points="0,0 12,0 0,22" fill="#111"/></svg>
    <a class="keyword col-a row-a" href="#"><span class="keyword__drip" role="img" aria-label="Dripping blood decoration"></span><span class="keyword__text">Blood Glucose</span></a>
    <a class="keyword col-b row-a" href="#"><span class="keyword__drip" role="img" aria-label="Dripping blood decoration"></span><span class="keyword__text">Blood Sugar Levels Chart</span></a>
    <a class="keyword col-a row-b" href="#"><span class="keyword__drip" role="img" aria-label="Dripping blood decoration"></span><span class="keyword__text">Normal Blood Sugar Range</span></a>
    <a class="keyword col-b row-b" href="#"><span class="keyword__drip" role="img" aria-label="Dripping blood decoration"></span><span class="keyword__text">Normal Blood Sugar Range</span></a>
  </section>

  <section class="ad-unit ad-unit--three">
    <header class="ad-header">
      <h2 class="ad-title">Ads Related to Blood Glucose</h2>
      <span class="ad-label">ADVERTISEMENT</span>
    </header>
    <svg class="ad-fold" viewBox="0 0 12 22"><polygon points="0,0 12,0 0,22" fill="#111"/></svg>
    <a class="keyword col-a row-a" href="#"><span class="keyword__drip" role="img" aria-label="Dripping blood decoration"></span><span class="keyword__text">Blood Glucose</span></a>
    <a class="keyword col-b row-a" href="#"><span class="keyword__drip" role="img" aria-label="Dripping blood decoration"></span><span class="keyword__text">Blood Sugar Levels Chart</span></a>
    <a class="keyword col-a row-b" href="#"><span class="keyword__drip" role="img" aria-label="Dripping blood decoration"></span><span class="keyword__text">Normal Blood Sugar Range</span></a>
    <a class="keyword col-b row-b" href="#"><span class="keyword__drip" role="img" aria-label="Dripping blood decoration"></span><span class="keyword__text">Normal Blood Sugar Range</span></a>
  </section>

</div>
</body>
</html>
```